Website homepage rework for women's travel website

I have a homepage (http://www.ladies-far-afield.com) that I'm 50% happy with but don't want to completely overhaul. I'd like to retain a similar look but upgrade it to something a bit more modern and less old-fashioned. The basic sense of the site is empowering, self-confident, fun and adventurous - but female and over 40.

A number of the elements on the page have to be redesigned, a few can be tweaked, and a few left alone. See the rest of the brief for further information.

Target Market(s)

women over 40 who like to travel

Industry/Entity Type

Travel

Number of Pages Required

1 page

Font styles to use
Other font styles liked:
• see my brief

Requirements
Must have
• - size - the page must be significantly wider
• - the only font I MUST keep is Raleway (as in the tagline) and possibly the font of the site name (Ladies Far Afield). Both of those work for me. There are too many fonts on the page, however, and that needs to be unified.
• - the rectangles I click to get inside the site have to change to something more modern, possibly square - they do not have to be separated into two columns as they are now, nor do they need the titles (toolkit etc)
• - I like the background image of the header - but it needs to be wider of course - also keep in mind the aspect - it has to fit into the smaller inside pages, whose size will not change
• - at the end of the project I need to receive the separate elements of the design so I can eventually make a change myself if needed ie. replace my own photo, for example
Nice to have
• - the three photos need to change to something more eye-popping - or something else should take their place to fill the space
Should not have
• I do not want a full, original redesign. I want my readers to still feel as though they are on the same site - same header, mostly same fonts.

```html
<!DOCTYPE html>
<html lang="en">
<head>
<meta charset="utf-8">
<title>Ladies Far Afield – Travel resources for women</title>
<link href="https://fonts.googleapis.com/css2?family=Raleway:wght@400;500;600&family=Open+Sans:wght@400&display=swap" rel="stylesheet">
<style>
  :root {
    --orange: #f7a03c;
    --orange-deep: #f06a12;
    --charcoal: #2a2a2a;
    --ink: #222222;
    --muted: #6f6f6f;
    --red: #c9301c;
    --panel: #f0f0f0;
    --rule: #cfcfcf;
    --white: #ffffff;
  }
  * { margin: 0; padding: 0; box-sizing: border-box; }
  html, body { width: 762px; height: 1200px; overflow: hidden; background: var(--white); }
  body { position: relative; font-family: "Raleway", sans-serif; color: var(--ink); }

  .hero { position: absolute; left: 0; top: 0; width: 762px; height: 312px; overflow: hidden; }
  .hero-scene {
    position: absolute; inset: 0;
    background:
      linear-gradient(180deg, rgba(0,0,0,0) 0 72%, rgba(110,100,95,0.0) 72%),
      linear-gradient(100deg, rgba(0,0,0,0) 0 44%, rgba(120,115,110,0.55) 47% 53%, rgba(0,0,0,0) 56%),
      linear-gradient(180deg, #fbd84a 0%, #f8b934 22%, #f39a2c 40%, #d9682a 50%, #a8472a 58%, #c77a48 66%, #9a6a4e 80%, #6e5e52 100%);
  }
  .hero-portrait {
    position: absolute; left: 405px; top: 30px; width: 357px; height: 282px;
    background:
      radial-gradient(ellipse 70px 85px at 150px 115px, #e9c4a8 0 60%, rgba(233,196,168,0) 100%),
      radial-gradient(ellipse 90px 70px at 150px 70px, #e8d9a6 0 55%, rgba(232,217,166,0) 100%),
      radial-gradient(ellipse 80px 60px at 155px 282px, #d8403a 0 60%, rgba(216,64,58,0) 100%),
      radial-gradient(ellipse 190px 150px at 150px 270px, #c9ccc0 0 65%, rgba(201,204,192,0) 100%);
  }
  .brand {
    position: absolute; left: 61px; top: 16px; width: 307px; height: 38px;
    background: linear-gradient(90deg, var(--orange-deep), #f48a22);
    color: var(--white); font-size: 29px; font-weight: 500; line-height: 38px;
    padding-left: 10px; letter-spacing: 0.3px;
  }
  .tagline { position: absolute; left: 60px; top: 57px; font-size: 16px; color: var(--ink); }
  .hero-title {
    position: absolute; left: 57px; top: 184px; color: var(--white);
    text-shadow: 0 1px 3px rgba(0,0,0,0.45);
  }
  .hero-title .caps { display: block; font-size: 25.5px; font-weight: 600; line-height: 32px; }
  .hero-title .name { display: block; font-size: 22px; font-weight: 400; line-height: 30px; letter-spacing: 0.5px; }

  .nav {
    position: absolute; left: 0; top: 312px; width: 762px; height: 38px;
    background: var(--orange); font-size: 10.5px; color: var(--white); text-transform: uppercase;
  }
  .nav a { color: inherit; text-decoration: none; position: absolute; top: 0; height: 38px; line-height: 38px; }
  .nav .current { left: 54px; width: 97px; background: var(--charcoal); text-align: center; }

  .intro { position: absolute; left: 50px; top: 383px; width: 420px; }
  .intro h1 { font-size: 12.5px; font-weight: 500; margin-bottom: 9px; }
  .intro li { list-style: none; font-size: 11.5px; color: #555; line-height: 24.5px; }
  .intro li span { color: var(--red); margin: 0 5px 0 4px; }

  .snapshots { position: absolute; left: 478px; top: 390px; width: 236px; height: 90px; }
  .snap {
    position: absolute; width: 76px; height: 76px; background: var(--white);
    box-shadow: 0 1px 4px rgba(0,0,0,0.3); padding: 4px 4px 12px;
  }
  .snap div { width: 100%; height: 100%; }
  .snap-line { position: absolute; left: 0; top: 0; z-index: 2; }

  .cta {
    position: absolute; left: 54px; top: 511px; width: 652px; height: 46px;
    border: 1px solid var(--rule); background: #f7f7f7;
    box-shadow: 0 1px 3px rgba(0,0,0,0.15);
    text-align: center; line-height: 44px; font-size: 17px; color: var(--ink);
  }
  .cta a { color: var(--red); text-decoration: none; }

  .section-title {
    position: absolute; left: 0; width: 762px; text-align: center;
    color: var(--red); font-size: 17px; font-weight: 400; letter-spacing: 0.5px;
  }
  .panel { position: absolute; left: 0; top: 849px; width: 762px; height: 263px; background: var(--panel); }

  .tile { position: absolute; width: 160px; text-align: center; }
  .tile .thumb {
    width: 104px; height: 104px; margin: 0 auto; border-radius: 50%;
    border: 2px solid var(--white); box-shadow: 0 0 0 1px #dddddd;
  }
  .tile h3 { font-size: 10.5px; font-weight: 400; margin-top: 13px; text-transform: uppercase; letter-spacing: 0.2px; }
  .tile p { font-size: 8.5px; color: var(--muted); margin-top: 4px; line-height: 12px; }

  .social { position: absolute; left: 336px; top: 1144px; display: flex; gap: 9px; }
  .social span { width: 15px; height: 15px; background: #555; border-radius: 2px; display: block; }
  .copyright {
    position: absolute; left: 0; top: 1170px; width: 762px; text-align: center;
    font-family: "Open Sans", sans-serif; font-size: 8px; color: #333;
  }
</style>
</head>
<body>

<header class="hero">
  <div class="hero-scene" role="img" aria-label="Header photo: straight desert road running towards red rock buttes under a yellow and orange sky, with a faint old map printed over the sky"></div>
  <div class="hero-portrait" role="img" aria-label="Portrait photo of the site founder, smiling, sunglasses on her head, wearing a light khaki shirt over a red top"></div>
  <div class="brand">Ladies Far Afield</div>
  <p class="tagline">For women who travel smart, safe + solo</p>
  <h2 class="hero-title"><span class="caps">TRAVEL RESOURCES FOR</span><span class="name">Ladies Far Afield</span></h2>
</header>

<nav class="nav">
  <a class="current" href="#">Start here</a>
  <a href="#" style="left:185px">About</a>
  <a href="#" style="left:274px">Travel resources</a>
  <a href="#" style="left:426px">Blog</a>
  <a href="#" style="left:507px">Travel shop</a>
  <a href="#" style="left:628px">Contact</a>
</nav>

<section class="intro">
  <h1>Hi, I’m Marta. I took my first solo trip at 15. I’ll show you how to travel…</h1>
  <ul>
    <li><span>»</span>Smart: practical tools to help you plan – and afford – the perfect trip</li>
    <li><span>»</span>Safe: down-to- earth advice and a ton of safety recommendations</li>
    <li><span>»</span>Solo: yes, you can do it!</li>
  </ul>
</section>

<div class="snapshots">
  <div class="snap" style="left:6px;top:2px;transform:rotate(-3deg)"><div role="img" aria-label="Photo: palm trees on a tropical beach by the sea" style="background:linear-gradient(180deg,#5fb4e6 0%,#3f8fc4 45%,#2e6a7a 60%,#2f5a26 80%,#1e3a18 100%)"></div></div>
  <div class="snap" style="left:82px;top:8px;transform:rotate(2deg)"><div role="img" aria-label="Photo: blue flower pots with green plants against an orange wall" style="background:linear-gradient(180deg,#e8903a 0%,#e6a24a 35%,#2f8fc8 55%,#3a7ab0 75%,#6a9a3a 100%)"></div></div>
  <div class="snap" style="left:154px;top:2px;transform:rotate(-1deg)"><div role="img" aria-label="Photo: red scooter parked in a colourful old street" style="background:linear-gradient(180deg,#7ab8dc 0%,#d8a890 35%,#c98a6a 55%,#b83a2e 75%,#5a6a3a 100%)"></div></div>
  <svg class="snap-line" width="236" height="90" aria-hidden="true">
    <path d="M2 70 Q40 88 90 80 T170 80 T234 68" fill="none" stroke="#444" stroke-width="1" stroke-dasharray="3 3"/>
  </svg>
</div>

<div class="cta">Thinking of solo travel? <a href="#">CLICK HERE</a> to find out how.</div>

<h2 class="section-title" style="top:604px">TRAVEL TOOLKIT</h2>

<article class="tile" style="left:43px;top:658px">
  <div class="thumb" role="img" aria-label="Photo: plated salmon dish with herbs" style="background:linear-gradient(150deg,#f2ece2 0%,#d8402a 30%,#2f7a2a 45%,#e0843a 60%,#f08a4a 78%,#f4eee6 100%)"></div>
  <h3>Eating with locals</h3><p>The Ultimate Guide to<br>Social Dining</p>
</article>
<article class="tile" style="left:210px;top:658px">
  <div class="thumb" role="img" aria-label="Photo: open suitcase with packed travel items" style="background:linear-gradient(170deg,#3a3a4a 0%,#c8a43a 25%,#8a2a2a 50%,#4a5a7a 70%,#1e2230 100%)"></div>
  <h3>Your packing list</h3><p>Take what you need - no more</p>
</article>
<article class="tile" style="left:387px;top:658px">
  <div class="thumb" role="img" aria-label="Photo: cruise ship decks lit blue at night" style="background:linear-gradient(160deg,#0c1026 0%,#1a2a6a 30%,#3c7ae8 50%,#1e3aa0 65%,#0c1026 100%)"></div>
  <h3>No single supplements</h3><p>17 ways to avoid paying it</p>
</article>
<article class="tile" style="left:556px;top:658px">
  <div class="thumb" role="img" aria-label="Photo: travel gear laid out on a table" style="background:linear-gradient(180deg,#c8c2b8 0%,#9a948a 35%,#c8506a 50%,#5a5650 70%,#2a2826 100%)"></div>
  <h3>Stress management</h3><p>How to travel stress free</p>
</article>

<div class="panel"></div>
<h2 class="section-title" style="top:877px">DESTINATIONS</h2>

<article class="tile" style="left:34px;top:929px">
  <div class="thumb" role="img" aria-label="Photo: blue lake among forested mountains" style="background:linear-gradient(180deg,#9ac4ec 0%,#5a8ab8 25%,#2f6aa8 45%,#2a5a8a 65%,#2a4a3a 85%,#1a2e22 100%)"></div>
  <h3>Solo to Argentina</h3><p>It doesn’t take two to tango</p>
</article>
<article class="tile" style="left:204px;top:929px">
  <div class="thumb" role="img" aria-label="Photo: grilled fish fillets with lemon on a white plate" style="background:radial-gradient(circle,#d89a56 0 35%,#c4884a 55%,#eeeae2 80%)"></div>
  <h3>European foodie</h3><p>9 top Destinations for October</p>
</article>
<article class="tile" style="left:380px;top:929px">
  <div class="thumb" role="img" aria-label="Photo: open green steppe below distant hills" style="background:linear-gradient(180deg,#8ab4d8 0%,#a8c4dc 20%,#7a7a6a 38%,#9a9a62 55%,#b0a660 75%,#8a8448 100%)"></div>
  <h3>Solo female travel</h3><p>3-Week Central Asia Itinerary</p>
</article>
<article class="tile" style="left:566px;top:929px">
  <div class="thumb" role="img" aria-label="Photo: black and white old town street" style="background:linear-gradient(90deg,#4a4a4a 0%,#9a9a9a 25%,#e0e0e0 50%,#8a8a8a 75%,#3a3a3a 100%)"></div>
  <h3>Rebellious Carouge</h3><p>Geneva’s Alter Ego ?</p>
</article>

<div class="social" aria-label="Social links">
  <span aria-label="Social link 1"></span><span aria-label="Social link 2"></span><span aria-label="Social link 3"></span><span aria-label="Social link 4"></span>
</div>
<p class="copyright">Copyright © 2016. All Rights Reserved</p>

</body>
</html>
```